Vesna Architecture

We are a architectural design and build company working between scales 1/1000 to 1/1 we want people to understand our difference from our design experience and quality.we build hotels restourants and office spaces.Our company name is Vesna architecture to mind sustainability.

We want to write our adress phone and work spesifications on the card and we want our logo as backround.

Ps:you could find the logo adress and phone box numbers from the web:www.vesnayapi.example

Target Market(s)

Who looks for experts.

Industry/Entity Type

Architecture

Requirements
Must have
• Design is over everything.
Should not have
• we don want it to be colorfull

```html
<!DOCTYPE html>
<html lang="en">
<head>
<meta charset="utf-8">
<title>Vesna Mimarlik — Business Card</title>
<link rel="stylesheet" href="https://fonts.googleapis.com/css2?family=Courier+Prime&family=Montserrat:wght@500&display=swap">
<style>
  :root {
    --backdrop: #2b0a0f;
    --card: #ffffff;
    --ink: #111111;
  }
  * { margin: 0; padding: 0; box-sizing: border-box; }
  html, body {
    width: 1200px;
    height: 601px;
    overflow: hidden;
    background: var(--backdrop);
  }
  .stage {
    position: relative;
    width: 1200px;
    height: 601px;
  }
  .card {
    position: absolute;
    top: 221px;
    width: 449px;
    height: 249px;
    background: var(--card);
    border-radius: 20px;
    color: var(--ink);
  }
  .card--front { left: 162px; }
  .card--back {
    left: 660px;
    display: flex;
    align-items: center;
    justify-content: center;
  }
  .wordmark {
    font-family: "Montserrat", sans-serif;
    font-weight: 500;
    color: var(--ink);
    line-height: 1;
  }
  .wordmark__name { display: block; letter-spacing: 1px; }
  .wordmark__sub { display: block; letter-spacing: 2px; }
  .card--front .wordmark {
    position: absolute;
    left: 42px;
    top: 24px;
  }
  .card--front .wordmark__name { font-size: 44px; }
  .card--front .wordmark__sub { font-size: 15px; margin-top: 8px; }
  .card--back .wordmark { text-align: left; margin-top: 6px; }
  .card--back .wordmark__name { font-size: 78px; }
  .card--back .wordmark__sub { font-size: 23px; margin-top: 14px; letter-spacing: 3px; }
  .contact {
    position: absolute;
    top: 176px;
    font-family: "Courier Prime", monospace;
    font-size: 10px;
    line-height: 11px;
    color: var(--ink);
    font-style: normal;
  }
  .contact--person { left: 42px; }
  .contact--studio { left: 286px; }
</style>
</head>
<body>
<main class="stage">
  <section class="card card--front" aria-label="Card front">
    <div class="wordmark">
      <span class="wordmark__name">vesna</span>
      <span class="wordmark__sub">MİMARLIK</span>
    </div>
    <p class="contact contact--person">SELIN ARAL<br>architecture</p>
    <address class="contact contact--studio">
      Vesna Mimarlik<br>
      PO Box 410<br>
      Tel:0090 212 555 0100<br>
      studio@vesnayapi.example
    </address>
  </section>
  <section class="card card--back" aria-label="Card back">
    <div class="wordmark">
      <span class="wordmark__name">vesna</span>
      <span class="wordmark__sub">MİMARLIK</span>
    </div>
  </section>
</main>
</body>
</html>
```